Law Firm Needs a new Website Design

We need a new website design for our law firm located in Manhattan (Law Offices of Tobias R. Venkland, PLLC).
We have an existing logo that we will to continue using, which can be found in www.VenklandLaw.example.
The Prime Counsel, Top Advocates Logo should also be reflected near the bottom of the Home page.
The website will be 6 pages.

Deliverables:
I want a
1) home page,
2) About Us/Practice Areas page,
3) attorneys,
4) News and Articles page, and
5) Contact and Directions/Privacy Policy page.

The colors of my logo should be in the website.
I also like a touch of black and red.

The website should project "excellence."
We seek to provide the highest quality legal services.
We handle estate planning, wills, trusts, planning for people with disabilities, asset protection and preservation, Medicaid planning, hospital safe discharge, nursing home placement, powers of attorney, health care proxies, living wills, guardianships, probate, estate administration and related litigation.

I would like the colors of my Logo used (including shading where appropriate).
I also want some black on the borders and/or bottom and some red touches throughout the page.

My Logo should appear everywhere that "Law Offices Of Tobias R. Venkland, PLLC" appears.
I want the badges for Prime counsel, Top Advocates, Top Legal Practices, and ZELQ on the Home page.
I do not want too much text on the home page.

We would also like the website to have coding.
The final design should also communicate quality, expertise and stability.
Great start so far by the people who submitted designs.
Thank you.

Industry/Entity Type

Law Firm

Coding

Coded - Design and coding required

Number of Pages Required

5+ page

Colors
3276b5
ec1f27
474747

Requirements
Must have
• Please use my logo each time you mention Law Offices of Tobias R. Venkland, PLLC. Please include the Primecounsel, Top Advocates, Top Legal Practices and Zelq rating Badges on the web home page. I only wish to be contacted by phone. I am not including testimonials and am only using the New York City address.
Nice to have
• Prefer illustrations to photos regarding practice areas
Should not have
• Testimonials, contact me by email, free consultation.

```html
<!DOCTYPE html>
<html lang="en">
<head>
<meta charset="utf-8">
<title>Law Offices of Tobias R. Venkland, PLLC</title>
<link rel="stylesheet" href="https://fonts.googleapis.com/css2?family=Cinzel:wght@700&family=Montserrat:wght@400;600;700&display=swap">
<style>
:root{
  --navy:#2b3152;
  --red:#b51f26;
  --text:#5a5d66;
  --heading:#1f2233;
  --light:#eef0f3;
  --panel:#e2e5ea;
  --news-bg:#e7e9ec;
  --rule:#c9ccd2;
  --white:#ffffff;
}
*{margin:0;padding:0;box-sizing:border-box}
html,body{width:1200px;height:3429px;overflow:hidden}
body{font-family:'Montserrat',sans-serif;color:var(--text);background:var(--white);position:relative}
section,header,footer{position:absolute;left:0;width:1200px}
.abs{position:absolute}
.serif{font-family:'Cinzel',serif;font-weight:700;color:var(--heading)}

/* header */
.site-header{top:0;height:103px;background:var(--white);box-shadow:0 2px 6px rgba(0,0,0,.08);z-index:2}
.social-bar{right:98px;top:0;width:172px;height:32px;background:var(--navy);display:flex;justify-content:center;align-items:center;gap:22px}
.social-bar span{width:11px;height:11px;border-radius:50%;background:var(--white)}
.brand{left:98px;top:34px;display:flex;align-items:center;gap:12px}
.brand-mark{width:36px;height:36px;background:var(--navy)}
.brand-name{font-weight:600;font-size:14px;color:var(--navy);white-space:nowrap}
.main-nav{left:460px;top:47px;display:flex;gap:34px;font-size:11.5px;font-weight:600;color:var(--heading)}
.main-nav .active{color:var(--red);border-bottom:2px solid var(--red);padding-bottom:6px}

/* hero */
.hero{top:103px;height:599px;background:linear-gradient(100deg,#3f6a64 0%,#5d8a80 40%,#7d6a4e 70%,#5a3b24 100%)}
.hero-title{left:98px;top:192px;font-size:48px;line-height:58px;color:var(--white);letter-spacing:1px}
.hero-sub{left:98px;top:323px;font-size:11px;font-weight:600;color:var(--white);letter-spacing:.2px}
.btn-outline{border:2px solid var(--white);color:var(--white);font-size:11px;font-weight:700;display:flex;align-items:center;justify-content:center}
.hero .btn-outline{left:98px;top:368px;width:153px;height:32px}
.hero-dots{left:1038px;top:562px;display:flex;gap:6px}
.hero-dots span{width:7px;height:7px;border-radius:50%;border:1px solid var(--white)}
.hero-dots span:first-child{background:var(--white)}

/* profile bar */
.profile-bar{top:702px;height:103px;background:var(--navy)}
.firm-profile{left:98px;top:18px;width:428px;height:71px;border:2px solid var(--white);color:var(--white);text-align:center;font-size:10.5px;line-height:17px;padding-top:7px}
.firm-profile strong{display:block;font-size:11px;margin-bottom:3px}
.firm-profile em{font-style:normal;color:#e3575c}
.dropdown{top:39px;height:34px;border:2px solid var(--white);color:var(--white);font-size:11px;font-weight:700;display:flex;align-items:center;justify-content:space-between;padding:0 16px}
.dropdown svg{width:10px;height:8px}

/* who we are */
.who{top:805px;height:617px;background:var(--light)}
.consult-panel{left:697px;top:0;width:503px;height:617px;background:var(--panel)}
.who-title{left:98px;top:78px;font-size:28px}
.who-text{left:98px;top:124px;width:522px;font-size:12.5px;line-height:23px}
.who-text p+p{margin-top:23px}
.who-text .name{color:var(--red)}
.btn-red{border:2px solid var(--red);color:var(--red);font-size:11px;font-weight:700;display:flex;align-items:center;justify-content:center}
.who .btn-red{left:98px;top:505px;width:153px;height:34px}
.consult-title{left:103px;top:86px;font-size:18px}
.field{left:103px;width:299px;background:var(--white);border:1px solid #d5d8de;font-size:11px;color:#8a8d96;padding:12px 14px}
.submit{left:103px;top:502px;width:299px;height:39px;background:var(--navy);color:var(--white);font-size:12px;font-weight:700;display:flex;align-items:center;justify-content:center}

/* legal help */
.legal-help{top:1422px;height:247px;background:linear-gradient(90deg,#1b1b1d,#3b3a38 50%,#1d1d1f);text-align:center}
.legal-help h2{position:absolute;left:0;width:1200px;top:50px;font-size:27px;color:var(--white)}
.legal-help p{position:absolute;left:0;width:1200px;top:98px;font-size:16px;color:#e1e1e1}
.legal-help .btn-outline{left:489px;top:146px;width:222px;height:34px}

/* services */
.services{top:1669px;height:644px;background:var(--white)}
.section-title{font-size:31px}
.services .section-title{left:98px;top:71px}
.section-sub{left:98px;top:115px;font-size:22px;color:#444}
.services .rule{left:98px;top:160px;width:1001px;height:4px;background:var(--rule)}
.service{width:290px}
.service h3{font-size:16.5px;font-weight:700;color:var(--heading);border-left:4px solid var(--red);padding-left:8px;line-height:18px}
.service p{font-size:12px;line-height:22px;color:#8a8d96;margin-top:8px}
.services .btn-red{left:816px;top:482px;width:162px;height:32px}

/* news */
.news{top:2313px;height:594px;background:var(--news-bg)}
.news .section-title{left:98px;top:65px}
.news .section-sub{top:109px;font-size:12px;font-weight:600;color:#444}
.card{top:156px;width:272px}
.card-photo{width:272px;height:189px;background:linear-gradient(135deg,#6e5a45,#3d3b40)}
.card-avatar{left:184px;top:143px;width:84px;height:84px;border-radius:50%;border:4px solid var(--white);background:#9b8a7c}
.card .meta{margin-top:28px;font-size:11px;color:#444}
.card h3{margin-top:16px;font-size:17px;font-weight:700;color:var(--heading)}
.card p{margin-top:10px;font-size:12px;line-height:22px;color:#8a8d96}
.card .more{margin-top:12px;font-size:12px;color:var(--red)}

/* partners */
.partners{top:2907px;height:128px;background:#eff0f2}
.partners h2{left:98px;top:58px;font-size:22px}
.badge{top:46px;width:210px;height:44px;background:var(--white);border:2px solid #c9ccd3}
.badge-small{left:903px;top:18px;width:100px;height:92px;background:var(--white);border:2px solid #c9ccd3}
.partners .arrow{left:1078px;top:45px;width:20px;height:36px}

/* footer */
.site-footer{top:3035px;height:394px;background:#f4f5f7}
.footer-col h4{font-size:16px;font-weight:700;color:var(--heading);margin-bottom:14px}
.footer-col li{list-style:none;font-size:12px;line-height:27px;color:#555}
.address{font-size:12px;line-height:27px;color:#555}
.address .office{color:var(--red)}
.stay p{font-size:12px;line-height:23px;color:#555;width:270px}
.email-field{left:832px;top:161px;width:270px;height:42px;background:var(--white);border:1px solid #d2d5db;font-size:11px;color:#8a8d96;padding:14px}
.signup{left:992px;top:218px;width:110px;height:40px;background:var(--navy);color:var(--white);font-size:12px;font-weight:600;display:flex;align-items:center;justify-content:center}
.footer-rule{left:98px;top:330px;width:1004px;height:1px;background:#c9ccd2}
.footer-mark{left:582px;top:312px;width:36px;height:36px;background:var(--navy)}
.copyright{left:98px;top:355px;font-size:10px;color:#777}
.legal-links{left:844px;top:355px;font-size:10px;color:#777;display:flex;gap:28px}
</style>
</head>
<body>

<header class="site-header">
  <div class="abs social-bar" aria-label="Social links"><span></span><span></span><span></span><span></span></div>
  <div class="abs brand"><span class="brand-mark"></span><span class="brand-name">Law Offices of Tobias R. Venkland, PLLC</span></div>
  <nav class="abs main-nav">
    <span class="active">HOME</span><span>ABOUT</span><span>SERVICE</span><span>PRACTICE AREAS</span><span>PRIVACY POLICY</span><span>NEWS</span><span>CONTACT</span>
  </nav>
</header>

<section class="hero" role="img" aria-label="Bronze scales of justice on a wooden desk against a teal backdrop">
  <h1 class="abs serif hero-title">WELCOME<br>VENKLAND LAW</h1>
  <p class="abs hero-sub">WE CARE ABOUT OUR CLIENTS AND BELIEVE IN CULTIVATING LONG-TERM RELATIONSHIPS</p>
  <span class="abs btn-outline">LEARN MORE</span>
  <div class="abs hero-dots"><span></span><span></span><span></span><span></span><span></span></div>
</section>

<section class="profile-bar">
  <div class="abs firm-profile"><strong>FIRM PROFILE</strong>Our firm was founded in 1993 by <em>Tobias R. Venkland</em>, a member of<br>the National Guild of Elder Law</div>
  <div class="abs dropdown" style="left:651px;width:174px">ATTORNEYS<svg viewBox="0 0 10 8"><path d="M1 2l4 4 4-4" fill="none" stroke="#fff" stroke-width="1.6"/></svg></div>
  <div class="abs dropdown" style="left:857px;width:242px">CONTACT AND DIRECTIONS<svg viewBox="0 0 10 8"><path d="M1 2l4 4 4-4" fill="none" stroke="#fff" stroke-width="1.6"/></svg></div>
</section>

<section class="who">
  <h2 class="abs serif who-title">WHO WE ARE</h2>
  <div class="abs who-text">
    <p>Our firm was founded in 1993 by <span class="name">Tobias R. Venkland</span>, a member of the National Guild of Elder Law Counsel (NGELC) and an elder law practitioner for over 19 years. Our firm is uniquely positioned to provide quality legal advice and representation in regards to estate planning, wills, trusts, planning for people with disabilities, asset protection and preservation, Medicaid planning, hospital safe discharge, nursing home placement, powers of attorney, health care proxies, living wills, guardianships, probate, estate administration and related litigation.</p>
    <p>Our familiarity with entitlement programs such as Medicaid and the statutes and regulations pertaining to them, our sensitivity to the problems and needs of seniors and our access to geriatric care managers enable us to help families preserve their life savings while planning for the care of a spouse, a parent or loved one who has dementia, Alzheimer's or other long-term health care needs.</p>
  </div>
  <span class="abs btn-red">LEARN MORE</span>
  <div class="abs consult-panel">
    <h2 class="abs serif consult-title">CASE CONSULTATION</h2>
    <div class="abs field" style="top:139px;height:39px">Name</div>
    <div class="abs field" style="top:198px;height:39px">Phone</div>
    <div class="abs field" style="top:258px;height:222px">Message</div>
    <div class="abs submit">SUBMIT</div>
  </div>
</section>

<section class="legal-help" role="img" aria-label="Dim courthouse interior with columns and a marble statue">
  <h2 class="serif">LEGAL HELP ?</h2>
  <p>We Care About Our Clients and Believe in Cultivating Long-Term Relationships.</p>
  <span class="abs btn-outline">CONTACT US NOW</span>
</section>

<section class="services">
  <h2 class="abs serif section-title">OUR SERVICES</h2>
  <p class="abs section-sub">We Handle Estate Planning</p>
  <div class="abs rule"></div>
  <div class="abs service" style="left:98px;top:214px"><h3>WILLS</h3><p>Our Familiarity with Entitlement Programs Such as Medicaid and the Statutes and Regulations Pertaining to Them.</p></div>
  <div class="abs service" style="left:457px;top:214px"><h3>TRUSTS</h3><p>Our Familiarity with Entitlement Programs Such as Medicaid and the Statutes and Regulations Pertaining to Them.</p></div>
  <div class="abs service" style="left:816px;top:214px"><h3>MEDICAID PLANNING</h3><p>Our Familiarity with Entitlement Programs Such as Medicaid and the Statutes and Regulations Pertaining to Them.</p></div>
  <div class="abs service" style="left:98px;top:336px"><h3>POWERS OF ATTORNEY</h3><p>Our Familiarity with Entitlement Programs Such as Medicaid and the Statutes and Regulations Pertaining to Them.</p></div>
  <div class="abs service" style="left:457px;top:336px"><h3>PROBATE</h3><p>Our Familiarity with Entitlement Programs Such as Medicaid and the Statutes and Regulations Pertaining to Them.</p></div>
  <div class="abs service" style="left:816px;top:336px"><h3>LIVING WILLS</h3><p>Our Familiarity with Entitlement Programs Such as Medicaid and the Statutes and Regulations Pertaining to Them.</p></div>
  <div class="abs service" style="left:98px;top:459px"><h3>WILLS</h3><p>Our Familiarity with Entitlement Programs Such as Medicaid and the Statutes and Regulations Pertaining to Them.</p></div>
  <div class="abs service" style="left:457px;top:459px"><h3>HEALTH CARE PROXIES</h3><p>Our Familiarity with Entitlement Programs Such as Medicaid and the Statutes and Regulations Pertaining to Them.</p></div>
  <span class="abs btn-red">READ MORE</span>
</section>

<section class="news">
  <h2 class="abs serif section-title">LATEST NEWS</h2>
  <p class="abs section-sub">OUR FIRM WAS FOUNDED IN 1993 BY TOBIAS R. VENKLAND</p>
  <article class="abs card" style="left:98px">
    <div class="card-photo" role="img" aria-label="Courtroom hearing with a judge and attorneys"></div>
    <div class="abs card-avatar" role="img" aria-label="Author portrait"></div>
    <p class="meta">Posted April 3, 2016</p><h3>LATEST NEWS</h3>
    <p>We care about our clients and believe in cultivating long-term relationships...</p><p class="more">READ MORE</p>
  </article>
  <article class="abs card" style="left:457px">
    <div class="card-photo" role="img" aria-label="Hands in handcuffs" style="background:linear-gradient(135deg,#b8a89a,#5b6a86)"></div>
    <div class="abs card-avatar" role="img" aria-label="Author portrait"></div>
    <p class="meta">Posted April 3, 2016</p><h3>LATEST NEWS</h3>
    <p>We care about our clients and believe in cultivating long-term relationships...</p><p class="more">READ MORE</p>
  </article>
  <article class="abs card" style="left:816px">
    <div class="card-photo" role="img" aria-label="Judge holding scales of justice and a gavel" style="background:linear-gradient(135deg,#2a2a2e,#6d5a3e)"></div>
    <div class="abs card-avatar" role="img" aria-label="Author portrait" style="background:#c7765a"></div>
    <p class="meta">Posted April 3, 2016</p><h3>LATEST NEWS</h3>
    <p>We care about our clients and believe in cultivating long-term relationships...</p><p class="more">READ MORE</p>
  </article>
</section>

<section class="partners">
  <h2 class="abs serif">OUR PARTNER</h2>
  <div class="abs badge" style="left:373px" role="img" aria-label="Prime Counsel badge"></div>
  <div class="abs badge" style="left:642px" role="img" aria-label="Top Advocates badge"></div>
  <div class="abs badge-small" role="img" aria-label="Top Legal Practices badge"></div>
  <svg class="abs arrow" viewBox="0 0 20 36" aria-hidden="true"><path d="M3 2l14 16L3 34" fill="none" stroke="#b9bcc3" stroke-width="3"/></svg>
</section>

<footer class="site-footer">
  <div class="abs footer-col" style="left:98px;top:60px">
    <h4>SITE MAP</h4>
    <ul><li>Home</li><li>Practice Areas</li><li>Privacy Policy</li><li>Contact and Directions</li><li>News</li><li>Attorneys</li></ul>
  </div>
  <div class="abs footer-col" style="left:391px;top:60px">
    <h4>ADDRESS</h4>
    <div class="address"><span class="office">Manhattan Main Office :</span><br>218 Westbury Avenue Suite 1400<br>New York NY 10118<br>Tel: (212) 555-0148<br>Fax: (212) 555-0172</div>
  </div>
  <div class="abs footer-col stay" style="left:832px;top:60px">
    <h4>STAY CONNECTED</h4>
    <p>We care about our clients and believe in cultivating long-term relationships.</p>
  </div>
  <div class="abs email-field">Your Email Address</div>
  <div class="abs signup">SIGN UP</div>
  <div class="abs footer-rule"></div>
  <div class="abs footer-mark" role="img" aria-label="Law Offices of Tobias R. Venkland, PLLC"></div>
  <p class="abs copyright">Copyright© 2009-2016 Law Offices of Tobias R. Venkland, PLLC</p>
  <div class="abs legal-links"><span>PRIVACY POLICY</span><span>TERMS AND CONDITIONS</span></div>
</footer>

</body>
</html>
```